Poster Design for company teaching children how to cook

Bright Pantry is a local business providing 2 key services (and 1 lesser):
1. After School Cookery clubs
2. Parties
(3. Cookery Classes for pre-schoolers)
A good summary can be found at our website www.bright-pantry.co.uk
We want a poster that we can display at various events, for example, outside parties, alongside demonstrations and in schools. We also would like to replicate the design for advertisement use in press.
We want to communicate that our classes and parties are good fun whilst at the same time being great for children's confidence and skills.
Please contact me tom@bright-pantry.co.uk with any questions and for company logo files.

Now I have sorted out the wording as follows, thanks for your patience:

inspiring children to cook (n.b. lower case as is the wording in the logo)

Classes

- Create nutritious food from scratch that can be replicated at home

- Increase confidence and skills in the kitchen

- Promote awareness of the importance of a nutritionally balanced diet

Parties

- Let us take the stress and run the party for you by providing the entertainment at the same time as the catering

- A variety of sweet and savoury dishes to choose from

- Party bags and invitations included

Call Morwenna now on 07519 620387 for more information or visit www.bright-pantry.co.uk

Since the call to action now contains contact details these need not be repeated elsewhere

Target Market(s)

Children at our classes are generally in the primary school age group 6-11 year olds although our parties reach a slightly wider group 4-13.
We obviously look to appeal to this group directly but also appealing to their parents, the budget holders, should not be underestimated!

Requirements
Must have
• A strong image (please pick from attachments)
• Company logo
• Company contact details including website, email address and phone
• Strapline / Call to action (Wording to be confirmed)
• Two textual areas where we can describe the benefits from parties/classes (about 40-50 words maximum in each. Wording to be confirmed)
• Any use of colour needs to be consistent with the logo palette
• colours are CMYK - Navy & Caribbean Blue
• green - CMYK Mint Julep
• purple - CMYK Amethyst
• Blue - CMYK Caribbean Blue
• Purple light
• C 0
• M 100
• Y 0
• K 0
• Purple dark
• C 50
• M 100
• Y 0
• K 0
• Green light
• C 50
• M 0
• Y 100
• K 0
• Green dark
• C 75
• M 0
• Y 100
• K 25
• Blue light
• C 100
• M 0
• Y 0
• K 0
• Blue dark
• C 100
• M 50
• Y 0
• K 0
• Font in Logo is "Brasserie". Any other font used should be unfussy and clear.
Nice to have
• Subject to space and design, maybe a testimonial or two (Wording to be confirmed)
Should not have
• The image should dominate, not the company logo
• No cartoony illustrations

```html
<!DOCTYPE html>
<html lang="en">
<head>
<meta charset="utf-8">
<title>Bright Pantry – inspiring children to cook</title>
<link rel="stylesheet" href="https://fonts.googleapis.com/css2?family=Arimo:wght@400;700&display=swap">
<style>
  :root {
    --caribbean: #1b95b6;
    --navy: #1d3a6e;
    --mint: #8cc63e;
    --mint-faint: #dde9c8;
    --amethyst: #8a2b8f;
    --white: #ffffff;
  }
  * { margin: 0; padding: 0; box-sizing: border-box; }
  html, body { width: 849px; height: 1200px; overflow: hidden; background: var(--white); }
  body { font-family: "Arimo", Arial, sans-serif; }
  .poster { position: relative; width: 849px; height: 1200px; overflow: hidden; background: var(--white); }

  .hero-photo {
    position: absolute; left: 0; top: 0; width: 849px; height: 580px;
    background:
      radial-gradient(ellipse 260px 230px at 330px 250px, #e8c6a8 0%, rgba(232,198,168,0) 100%),
      radial-gradient(ellipse 260px 200px at 420px 330px, rgba(200,50,60,.55) 0%, rgba(200,50,60,0) 70%),
      radial-gradient(ellipse 320px 260px at 560px 480px, #7d9cc8 0%, rgba(125,156,200,0) 100%),
      linear-gradient(160deg, #d9b98e 0%, #efe3cf 40%, #e6d2bb 65%, #c9d3e3 100%);
  }
  .hero-mask { position: absolute; left: 0; top: 0; width: 849px; height: 1200px; }

  .brand { position: absolute; left: 30px; top: 500px; display: flex; align-items: center; gap: 12px; }
  .brand-dot { width: 34px; height: 34px; border-radius: 50%; background: var(--amethyst); }
  .brand-name { font-weight: 700; font-size: 38px; color: var(--caribbean); letter-spacing: -0.5px; }

  .strapline {
    position: absolute; left: 333px; top: 548px;
    font-weight: 700; font-size: 31px; color: var(--caribbean); letter-spacing: -0.2px;
  }

  .side-photo {
    position: absolute; left: 39px; top: 645px; width: 262px; height: 292px;
    border-radius: 12px 12px 0 0;
    background:
      radial-gradient(ellipse 120px 140px at 110px 170px, #e9c9ad 0%, rgba(233,201,173,0) 100%),
      radial-gradient(ellipse 90px 60px at 150px 50px, #fbfbfb 0%, rgba(251,251,251,0) 100%),
      linear-gradient(170deg, #b9b2a6 0%, #d8cbbb 45%, #7a5a45 80%, #2c8c8e 100%);
  }
  .testimonial {
    position: absolute; left: 39px; top: 937px; width: 262px; height: 130px;
    background: var(--navy); border-radius: 0 0 12px 12px;
    color: var(--white); font-size: 16.5px; line-height: 1.25; padding: 16px 14px 0 22px;
  }
  .testimonial cite { display: block; font-style: normal; padding-left: 48px; }

  .section-label {
    position: absolute; left: 317px; height: 30px; padding: 0 24px 0 12px;
    background: var(--caribbean); color: var(--white);
    font-weight: 700; font-size: 19.5px; line-height: 30px;
    border-radius: 4px 15px 15px 4px;
  }
  .section-label.classes { top: 644px; }
  .section-label.parties { top: 876px; }

  .benefits { position: absolute; left: 323px; width: 490px; list-style: none; color: var(--navy); font-size: 17.5px; line-height: 1.24; }
  .benefits li { padding-left: 11px; text-indent: -11px; margin-bottom: 24px; }
  .benefits li::before { content: "- "; }
  .benefits.classes { top: 690px; }
  .benefits.parties { top: 923px; }
  .benefits.parties li { margin-bottom: 22px; }

  .call-to-action {
    position: absolute; left: 0; top: 1137px; width: 849px; height: 63px;
    background: var(--mint); color: var(--white);
    font-weight: 700; font-size: 18.5px; text-align: center; line-height: 63px;
  }
</style>
</head>
<body>
<main class="poster">
  <div class="hero-photo" role="img" aria-label="Photo of a young boy in a chef's hat holding up a strawberry and banana fruit skewer"></div>

  <svg class="hero-mask" viewBox="0 0 849 1200" aria-hidden="true">
    <path d="M0 1200 L0 490 Q0 452 40 452 L268 452 Q305 452 318 488 L328 515 Q338 538 372 538 L849 538 L849 1200 Z" fill="#ffffff"/>
  </svg>

  <div class="brand">
    <span class="brand-dot"></span>
    <span class="brand-name">Bright Pantry</span>
  </div>
  <p class="strapline">inspiring children to cook</p>

  <div class="side-photo" role="img" aria-label="Photo of a little girl in a chef's hat preparing food"></div>
  <blockquote class="testimonial">
    “All of the kids were having fun&nbsp; and the best part is it’s the most worry free party we ever had for Rosie. ”
    <cite>- Peter &amp; Jane Hollis</cite>
  </blockquote>

  <h2 class="section-label classes">Classes</h2>
  <ul class="benefits classes">
    <li>Create nutritious food from scratch that can be replicated at home</li>
    <li>Increase confidence and skills in the kitchen</li>
    <li>Promote awareness of the importance of a nutritionally balanced diet</li>
  </ul>

  <h2 class="section-label parties">Parties</h2>
  <ul class="benefits parties">
    <li>Let us take the stress and run the party for you by providing the entertainment at the same time as the catering</li>
    <li>A variety of sweet and savoury dishes to choose from</li>
    <li>Party bags and invitations included</li>
  </ul>

  <p class="call-to-action">Call Morwenna now on 07519 620387 for more information or visit www.bright-pantry.co.uk</p>
</main>
</body>
</html>
```